International Food Manufacturer in the need of a new business card and logo.

Our Company - Northgate Pantry Ltd.

Our Industry - Food and Drink

We are a Wild Harvested Food Distributor / Manufacturer. We service the following food sectors: Supermarkets, Hotels, Restaurants, Cafes, Catering and all people looking to eat healthy food products.

Slogan - Wild harvested goodness for every table

Business card details -

48-52 Marlow Lane
Hatherby Green
London
EC9Z 4RT United Kingdom
Dennis Prowle
+44 7000 481736 - UK
+971 50 7739205 - UAE
+38 063 914 2758 - Ukraine
dennis@northgatepantry.example
www.northgatepantry.example

Goal - We are looking for a dynamic modern new look for our corporate image and a designer who can bring this new concept to our future food product designs. Please try to incorporate 3d hexagonal vector Imaging in your design concepts.

Target Market(s)

Industry/Entity Type

Food Service

Contact Information for Business Card

Northgate Pantry Ltd.
48-52 Marlow Lane
Hatherby Green
London
EC9Z 4RT United Kingdom
Dennis Prowle
+44 7000 481736 - UK
+971 50 7739205 - UAE

Font styles to use
Serif

Colors

Designer to choose colors to be used in the design.

Requirements
Must have
• Please read project description above.
Nice to have
Should not have

```html
<!DOCTYPE html>
<html lang="en">
<head>
<meta charset="utf-8">
<title>Northgate Pantry Ltd. – Business Card</title>
<link rel="stylesheet" href="https://fonts.googleapis.com/css2?family=Cinzel:wght@600;700&family=EB+Garamond:ital,wght@0,400;0,500;1,400&display=swap">
<style>
  :root {
    --backdrop: #e9e6e0;
    --card: #ffffff;
    --green-deep: #1f7a3a;
    --green-bright: #3aa845;
    --green-band: #35ad47;
    --green-band-dark: #1e8a37;
    --ink: #2d2d2d;
    --rule: #9aa59c;
  }
  * { box-sizing: border-box; margin: 0; padding: 0; }
  html, body { width: 900px; height: 1200px; overflow: hidden; }
  body {
    background: var(--backdrop);
    position: relative;
    font-family: "EB Garamond", Georgia, serif;
    color: var(--ink);
  }
  .card {
    position: absolute;
    left: 82px;
    width: 736px;
    height: 432px;
    background: var(--card);
    border-radius: 36px;
    overflow: hidden;
    box-shadow: 0 6px 18px rgba(0,0,0,0.18);
  }
  .card--front { top: 130px; }
  .card--back { top: 633px; }

  .company {
    position: absolute;
    left: 0; right: 0;
    text-align: center;
    font-family: "Cinzel", "Times New Roman", serif;
    font-weight: 700;
    font-size: 31px;
    letter-spacing: 1px;
    color: var(--green-deep);
    white-space: nowrap;
  }
  .slogan {
    position: absolute;
    left: 0; right: 0;
    text-align: center;
    font-style: italic;
    font-size: 30px;
    color: var(--green-bright);
    white-space: nowrap;
  }
  .card--front .company { top: 46px; }
  .card--front .slogan { top: 82px; }

  .brand-mark {
    position: absolute;
    display: flex;
    align-items: center;
    justify-content: center;
    gap: 10px;
    font-family: "EB Garamond", Georgia, serif;
    font-weight: 500;
    font-size: 24px;
    color: var(--green-deep);
    white-space: nowrap;
  }
  .brand-mark__dot {
    width: 22px; height: 22px;
    border-radius: 50%;
    background: var(--green-bright);
    flex: none;
  }
  .card--front .brand-mark { left: 110px; width: 230px; top: 226px; }
  .card--back .brand-mark { left: 0; right: 0; top: 150px; font-size: 30px; }
  .card--back .brand-mark__dot { width: 28px; height: 28px; }

  .divider {
    position: absolute;
    left: 342px; top: 158px;
    width: 1px; height: 162px;
    background: var(--rule);
  }
  .contact {
    position: absolute;
    left: 362px; top: 158px;
  }
  .contact__name {
    font-family: "Cinzel", "Times New Roman", serif;
    font-weight: 600;
    font-size: 21px;
    color: var(--green-deep);
    line-height: 1.1;
  }
  .contact__role {
    font-size: 12px;
    letter-spacing: 0.5px;
    color: var(--green-bright);
    margin-bottom: 11px;
  }
  .contact__list { list-style: none; }
  .contact__item {
    display: flex;
    align-items: center;
    gap: 7px;
    font-size: 16.5px;
    height: 23px;
    white-space: nowrap;
  }
  .contact__icon { width: 16px; height: 18px; flex: none; }

  .address-band {
    position: absolute;
    left: 0; right: 0;
    top: 382px; height: 34px;
  }
  .address-band svg { position: absolute; inset: 0; width: 100%; height: 100%; }
  .address-band__text {
    position: absolute;
    inset: 0;
    display: flex;
    align-items: center;
    justify-content: center;
    color: #ffffff;
    font-size: 16.5px;
    white-space: nowrap;
  }

  .card--back .company { top: 286px; }
  .card--back .slogan { top: 322px; }
</style>
</head>
<body>
  <svg width="0" height="0" style="position:absolute">
    <defs>
      <symbol id="hex-badge" viewBox="0 0 16 18">
        <polygon points="8,0 16,4.5 16,13.5 8,18 0,13.5 0,4.5" fill="#3aa845"/>
      </symbol>
    </defs>
  </svg>

  <section class="card card--front">
    <h1 class="company">NORTHGATE PANTRY LTD</h1>
    <p class="slogan">Wild harvested goodness for every table</p>

    <div class="brand-mark"><span class="brand-mark__dot"></span>Northgate Pantry</div>

    <div class="divider"></div>
    <div class="contact">
      <p class="contact__name">DENNIS PROWLE</p>
      <p class="contact__role">PRESIDENT</p>
      <ul class="contact__list">
        <li class="contact__item">
          <svg class="contact__icon" viewBox="0 0 16 18"><use href="#hex-badge"/><path d="M5 5.5c0 4 2.5 7 6 7.5l1-1.6-1.8-1-0.9 0.9c-1.2-0.5-2.2-1.6-2.6-2.8l0.9-0.8-0.9-1.9z" fill="#fff"/></svg>
          +44 7000 481736 - UK
        </li>
        <li class="contact__item">
          <svg class="contact__icon" viewBox="0 0 16 18"><use href="#hex-badge"/><path d="M5 5.5c0 4 2.5 7 6 7.5l1-1.6-1.8-1-0.9 0.9c-1.2-0.5-2.2-1.6-2.6-2.8l0.9-0.8-0.9-1.9z" fill="#fff"/></svg>
          +971 50 7739205 - UAE
        </li>
        <li class="contact__item">
          <svg class="contact__icon" viewBox="0 0 16 18"><use href="#hex-badge"/><path d="M5 5.5c0 4 2.5 7 6 7.5l1-1.6-1.8-1-0.9 0.9c-1.2-0.5-2.2-1.6-2.6-2.8l0.9-0.8-0.9-1.9z" fill="#fff"/></svg>
          +38 063 914 2758 - Ukraine
        </li>
        <li class="contact__item">
          <svg class="contact__icon" viewBox="0 0 16 18"><use href="#hex-badge"/><rect x="4" y="6" width="8" height="6" fill="none" stroke="#fff" stroke-width="1.2"/><path d="M4 6l4 3.2 4-3.2" fill="none" stroke="#fff" stroke-width="1.2"/></svg>
          dennis@northgatepantry.example
        </li>
        <li class="contact__item">
          <svg class="contact__icon" viewBox="0 0 16 18"><use href="#hex-badge"/><circle cx="8" cy="9" r="4" fill="none" stroke="#fff" stroke-width="1.2"/><path d="M4 9h8M8 5c-2 2.5-2 5.5 0 8M8 5c2 2.5 2 5.5 0 8" fill="none" stroke="#fff" stroke-width="0.9"/></svg>
          www.northgatepantry.example
        </li>
      </ul>
    </div>

    <div class="address-band">
      <svg viewBox="0 0 736 34" preserveAspectRatio="none">
        <rect width="736" height="34" fill="var(--green-band)"/>
        <polygon points="92,0 680,0 648,34 60,34" fill="var(--green-band-dark)"/>
      </svg>
      <p class="address-band__text">48-52 Marlow Lane, Hatherby Green, London, EC9Z 4RT United Kingdom</p>
    </div>
  </section>

  <section class="card card--back">
    <div class="brand-mark"><span class="brand-mark__dot"></span>Northgate Pantry</div>
    <h2 class="company">NORTHGATE PANTRY LTD</h2>
    <p class="slogan">Wild harvested goodness for every table</p>
  </section>
</body>
</html>
```